Car rental website design for a UAE car rental company

This project is about creating a new website design for a car rental company located in Dubai (United Arab Emirates), I opened the same project a few months ago but I didn't receive a lot of appealing entries so I closed it but this time I am marking the project as guaranteed to avoid such situation again, if you have already provided a design before then please re-submit again on this project so that it is considered while reviewing all the designs

A few important things:

1- We need a simple non-complex design
2- The final deliverable would be 2 screens (PSD, JPEG ... etc), the first screen is for the home page and the second screen is for an internal page
3- The home page must have a section that end users can use to rent a car online directly from the home page instead of going into some inner pages
4- The current website is very old and not very appealing so avoid creating a similar design (www.quarvin-drive.example)
5- The name is Quarvin but the company rents normal cars (no Limousin cars will be rented) so avoid adding any fancy cars in the images/graphics used in the design, just normal end users cars
6- The expected pages would be: home, About us, Our team, Strategy, Contact us and links to social media pages
7- The attachments include the company's logo and some screens from other car rental companies that provide online rentals/payments

If you have any questions please feel free to ask and please note that we will need the designs urgently

Thanks

Target Market(s)

Dubai - United Arab Emirates

Industry/Entity Type

It Company

Number of Pages Required

2 page

Font styles to use
Sans Serif

Requirements
Must have
• Check the project details
Nice to have
Should not have

```html
<!DOCTYPE html>
<html lang="en">
<head>
<meta charset="utf-8">
<title>Quarvin Rent A Car</title>
<link rel="stylesheet" href="https://fonts.googleapis.com/css2?family=PT+Sans:wght@400;700&family=Tinos:wght@400;700&display=swap">
<style>
:root{
  --crimson:#a3143a;
  --crimson-dark:#8a0f30;
  --ink:#2b2b2b;
  --grey:#6b6b6b;
  --line:#d9d9d9;
  --card-bg:#f7f7f7;
  --nav-bg:#ececec;
  --white:#ffffff;
  --button-dark:#1e1e1e;
}
*{box-sizing:border-box;margin:0;padding:0}
html,body{width:1200px;height:1012px;overflow:hidden;background:var(--white)}
body{position:relative;font-family:"PT Sans",Arial,sans-serif;color:var(--ink)}
.top-rule{position:absolute;left:0;top:0;width:1200px;height:4px;background:var(--crimson)}
.bottom-band{position:absolute;left:0;bottom:0;width:1200px;height:6px;background:#9a9a9a}

.brand{position:absolute;left:169px;top:22px;display:flex;align-items:center;gap:12px}
.brand-mark{width:52px;height:52px;background:var(--crimson)}
.brand-text{display:flex;flex-direction:column;line-height:1}
.brand-name{font-family:"Tinos",serif;font-size:34px;color:#7a7a7a}
.brand-tag{font-family:"Tinos",serif;font-weight:700;font-size:17px;color:var(--crimson);margin-top:3px;padding-left:28px;letter-spacing:.5px}

.call{position:absolute;left:824px;top:25px;display:flex;align-items:center;gap:8px}
.call-label{font-size:16px;color:var(--ink);line-height:1}
.call-number{font-size:29px;color:var(--ink);line-height:1.05}

.main-nav{position:absolute;left:153px;top:98px;width:895px;height:44px;border:1px solid #c9c9c9;border-radius:3px;background:linear-gradient(#f6f6f6,#dedede);box-shadow:0 1px 2px rgba(0,0,0,.15)}
.main-nav a{position:absolute;top:12px;font-family:"Tinos",serif;font-size:18px;color:var(--ink);text-decoration:none;letter-spacing:.4px}
.main-nav a.active{color:var(--crimson)}
.main-nav .sep{position:absolute;top:12px;width:1px;height:20px;background:#b5b5b5}
.social{display:flex;gap:4px}
.main-nav .social{position:absolute;left:768px;top:8px}
.social span{display:block;border-radius:50%}
.main-nav .social span{width:26px;height:26px}

.hero{position:absolute;left:153px;top:162px;width:894px;height:385px;background:linear-gradient(120deg,#6d7a86 0%,#1f2a4a 35%,#15204a 55%,#3a4250 100%)}
.hero-info{position:absolute;right:0;top:0;width:292px;height:385px;background:rgba(10,10,12,.72);color:var(--white);padding:54px 20px 0 26px}
.hero-title{font-size:26px;font-weight:400}
.hero-text{font-size:13.5px;line-height:17px;margin-top:4px}
.hero-price{font-size:26px;margin-top:24px;line-height:1}
.hero-note{font-size:11px;text-transform:uppercase;margin-top:4px}
.dots{position:absolute;left:26px;top:350px;display:flex;gap:5px}
.dots span{width:8px;height:8px;border-radius:50%;background:var(--white)}
.dots span.off{background:#8a8a8a}

.card{position:absolute;top:594px;width:279px;height:237px;border:1px solid #d6d6d6;border-radius:4px;background:linear-gradient(var(--white),var(--card-bg));padding:14px 14px 0 14px}
.card-title{font-family:"Tinos",serif;font-size:38px;line-height:1;color:var(--crimson)}
.card-sub{font-size:19px;line-height:1.1;text-transform:uppercase}
.card-body{font-size:11.4px;line-height:17px;text-transform:uppercase;margin-top:12px}
.btn{position:absolute;left:16px;bottom:14px;width:110px;height:32px;border-radius:2px;background:var(--crimson);color:var(--white);font-size:13px;text-transform:uppercase;display:flex;align-items:center;justify-content:center;border:0}
.offers{left:163px}
.gifts{left:458px}
.search{position:absolute;left:752px;top:594px;width:279px;height:237px;border-radius:4px;background:var(--crimson);color:var(--white);padding:14px 19px 0 19px}
.search .card-title,.search .card-sub{color:var(--white)}
.select{margin-top:8px;width:240px;height:27px;background:var(--white);border:1px solid #c7c7c7;font-size:11px;color:#9a9a9a;text-transform:uppercase;display:flex;align-items:center;justify-content:space-between;padding:0 6px}
.select:first-of-type{margin-top:14px}
.select i{width:14px;height:14px;background:#cfcfcf;border:1px solid #b0b0b0}
.search .btn{left:19px;background:var(--button-dark);bottom:26px}

.rule{position:absolute;left:159px;width:878px;height:1px;background:var(--line)}
.contact-col{position:absolute;top:884px}
.contact-col h3{font-size:19px;font-weight:400;text-transform:uppercase;color:var(--ink)}
.contact-col p{font-size:12.5px;color:var(--grey);margin-top:6px}

.footer-nav a{position:absolute;top:974px;font-size:12px;color:var(--ink);text-decoration:none;text-transform:uppercase}
.footer-nav a.active{color:var(--crimson)}
.footer-nav .sep{position:absolute;top:973px;width:1px;height:16px;background:#c9c9c9}
.footer-social{position:absolute;left:617px;top:970px}
.footer-social span{width:20px;height:20px;border:1.5px solid #444}
.footer-social span:first-child{border-color:var(--crimson)}
.copyright{position:absolute;left:781px;top:974px;font-size:12px;color:var(--ink)}
</style>
</head>
<body>
<div class="top-rule"></div>

<header>
  <div class="brand">
    <div class="brand-mark"></div>
    <div class="brand-text">
      <span class="brand-name">Quarvin</span>
      <span class="brand-tag">Rent A Car</span>
    </div>
  </div>
  <div class="call">
    <svg width="46" height="46" viewBox="0 0 46 46" aria-hidden="true">
      <circle cx="23" cy="23" r="21" fill="none" stroke="var(--crimson)" stroke-width="3"/>
      <path d="M15 13c2-2 4-1 5 1l2 4c1 2 0 3-1 4l-1 1c1 3 3 5 6 6l1-1c1-1 2-2 4-1l4 2c2 1 3 3 1 5l-2 2c-9 1-20-10-19-19z" fill="var(--crimson)"/>
    </svg>
    <div>
      <div class="call-label">CALL US NOW:</div>
      <div class="call-number">123-456-7890</div>
    </div>
  </div>

  <nav class="main-nav">
    <a class="active" style="left:20px" href="#">HOME</a>
    <span class="sep" style="left:103px"></span>
    <a style="left:127px" href="#">ABOUT US</a>
    <span class="sep" style="left:245px"></span>
    <a style="left:271px" href="#">OUR TEAM</a>
    <span class="sep" style="left:398px"></span>
    <a style="left:428px" href="#">STRATEGY</a>
    <span class="sep" style="left:557px"></span>
    <a style="left:589px" href="#">CONTACT US</a>
    <div class="social">
      <span style="background:#2bb3e6"></span>
      <span style="background:#3b5a99"></span>
      <span style="background:#555"></span>
      <span style="background:#1f7fb6"></span>
    </div>
  </nav>
</header>

<section class="hero" role="img" aria-label="Rear view of a dark blue rental car parked on a street">
  <div class="hero-info">
    <h2 class="hero-title">BME-612</h2>
    <p class="hero-text">Lorem ipsum dolor sit amet, consectetur adipiscing elit, sed do eiusmobjdg tempor incididunt ut labore et dolore mghfhgjagna aliqua. Ut enim ad minim veniaghgm, quis nostrud exercitation ullamco laboris nisi ut aliquip ex ea commodo consequhdhat. Duis aute irure dolor in reprehend dfghdgerit in voluptate velit esse cillum.</p>
    <div class="hero-price">$1.229</div>
    <div class="hero-note">300 km included per day</div>
    <div class="dots"><span></span><span class="off"></span><span></span><span></span></div>
  </div>
</section>

<article class="card offers">
  <h2 class="card-title">SPECIAL</h2>
  <div class="card-sub">Offers &amp; Packages</div>
  <p class="card-body">Lorem ipsum dolor sit amet conse ctedfitur dipis icing elit, sed do eiusmod tem dsfgsdfg ddpor incididunt ut labore et dvhfhfholore ddfhg dmagna aliqua. Ut ehjkhfgjhfjhf nim ad minim veniam.</p>
  <button class="btn">Read More</button>
</article>

<article class="card gifts">
  <h2 class="card-title">GIFT</h2>
  <div class="card-sub">Certificates</div>
  <p class="card-body">Lorem ipsum dolor sit amet conse ctedfitur dipis icing elit, sed do eiusmod tem dsfgsdfg ddpor incididunt ut labore et dvhfhfholore ddfhg dmagna aliqua. Ut ehjkhfgjhfjhf nim ad minim veniam.</p>
  <button class="btn">Read More</button>
</article>

<form class="search">
  <h2 class="card-title">SEARCH</h2>
  <div class="card-sub">Calculate and Book</div>
  <div class="select">All car types<i></i></div>
  <div class="select">All car brands<i></i></div>
  <div class="select">All car models<i></i></div>
  <button class="btn" type="button">Search Now</button>
</form>

<div class="rule" style="top:863px"></div>

<section>
  <div class="contact-col" style="left:166px">
    <h3>Address:</h3>
    <p>Sed ut perspiciatis unde omSed ut perspiciatis</p>
  </div>
  <div class="contact-col" style="left:479px">
    <h3>Phone:</h3>
    <p>+1(234) 567-8901; +1(234) 567-8902</p>
  </div>
  <div class="contact-col" style="left:766px">
    <h3>E-mail:</h3>
    <p>support@quarvin-drive.example</p>
  </div>
</section>

<div class="rule" style="top:954px"></div>

<footer>
  <nav class="footer-nav">
    <a class="active" style="left:163px" href="#">Home</a>
    <span class="sep" style="left:207px"></span>
    <a style="left:222px" href="#">About us</a>
    <span class="sep" style="left:288px"></span>
    <a style="left:304px" href="#">Our team</a>
    <span class="sep" style="left:375px"></span>
    <a style="left:392px" href="#">Strategy</a>
    <span class="sep" style="left:459px"></span>
    <a style="left:476px" href="#">Contact us</a>
  </nav>
  <div class="social footer-social"><span></span><span></span><span></span><span></span></div>
  <div class="copyright">© 2015. <b>Quarvin Rent A Car.</b> All Rights Reserved.</div>
</footer>

<div class="bottom-band"></div>
</body>
</html>
```